Buch-/E-Book-Cover
Zielgruppe
Wir verkaufen Trainings und vermitteln über unser Buch ein erstes vertieftes Wissen zum Thema Vermögensaufbau.
Aufgabenstellung
Es soll schlicht und schön sein, Angelehnt an Tall coin short coin, bzw. an Schau hin und bleib Klug von Bartholo Fenwick.
Wir benötigen die AI, etc Dateien und die fertigen Dateien für Velmora.de Lumora sowie Velmora.de Books (ehemals Printvale) mit fertigem Cover.
Vorgaben von Velmora.de über die Homepage. Anbei ein Beispiel (wegen Velmora.de Buchnummer etc) Abstände, Buchrücken etc.
Buch ca. 150 Seiten
https://www.velmora-beispiel.de/Gaertner-bleiben-heute-Zeichen-guten/dp/7392058164 Front und Backcover kann man sich da ansehen.
Der Buchtitel ist 'Baue Kredite und bleib frei' - - Lassen Sie uns freundschaftlich in entspannter Atmosphäre über Immobilien sprechen (der nebentitel so klein wie bei Tall Coin - Short Coin)
Rücktitel: Bitte zuerst Platzhalter.
Ich bitte um 5x8 inch, also wie DIN A 5, wir nehmen cremefarbenes Papier denke ich. Die Seitenzahl kann ich auf die Seite noch nicht sagen, wir haben aber 75 Din A4 Seiten, sprich nach Formatierung eher 160-165 Din A5. WErde ich Ihnen final nach dem Gewinn sagen.
Versuchen Sie mich mal aus dem einen Bild raus zu schneiden, und dass dann mit einem Layer über das cover zu legen.
2-3 Versionen wäre gut, mit 2-3 Bildern. Buchrücken ein kleines Bild von mir.
Seite vom Buch: Titel nochmal.

```html
<!DOCTYPE html>
<html lang="de">
<head>
<meta charset="utf-8">
<title>Baue Kredite und bleib frei – Buchumschlag</title>
<link rel="stylesheet" href="https://fonts.googleapis.com/css2?family=Open+Sans:wght@600;700;800&display=swap">
<style>
  :root {
    --navy-deep: #01061a;
    --navy: #06215e;
    --blue: #1d4fa6;
    --blue-light: #7aa3dc;
    --title-yellow: #fbd521;
    --text-white: #ffffff;
    --text-grey: #e4e8f0;
    --barcode-field: #ffffff;
    --jacket-brown: #4a3324;
    --shirt-light: #dfe7f2;
  }
  html, body {
    margin: 0;
    padding: 0;
    width: 1200px;
    height: 927px;
    overflow: hidden;
    background: var(--navy-deep);
  }
  .cover-wrap {
    position: relative;
    width: 1200px;
    height: 927px;
    overflow: hidden;
    font-family: "Open Sans", sans-serif;
    background:
      radial-gradient(ellipse 520px 420px at 830px 120px, rgba(122,163,220,0.95) 0%, rgba(60,110,190,0.7) 40%, rgba(29,79,166,0) 100%),
      radial-gradient(ellipse 700px 600px at 950px 400px, rgba(29,79,166,0.85) 0%, rgba(6,33,94,0.4) 60%, rgba(6,33,94,0) 100%),
      linear-gradient(160deg, #0e2f78 0%, #06215e 35%, #020a26 70%, #01061a 100%);
  }
  .barcode-field {
    position: absolute;
    left: 325px;
    top: 754px;
    width: 223px;
    height: 130px;
    background: var(--barcode-field);
  }
  .author-photo {
    position: absolute;
    left: 626px;
    top: 286px;
    width: 281px;
    height: 641px;
    border-radius: 120px 120px 0 0;
    background: linear-gradient(180deg, #3a2a20 0%, #c9a68c 12%, #b08a70 22%, var(--shirt-light) 35%, var(--jacket-brown) 55%, #2e2018 100%);
    opacity: 0.9;
  }
  .typography {
    position: absolute;
    inset: 0;
  }
  .title-word { font-weight: 800; fill: var(--title-yellow); }
  .author-line { font-weight: 800; fill: var(--text-white); }
  .series-small { font-weight: 600; fill: var(--text-grey); letter-spacing: 1.5px; }
  .series-large { font-weight: 700; fill: var(--text-white); }
  .subtitle { font-weight: 600; fill: var(--text-white); }
</style>
</head>
<body>
<div class="cover-wrap">
  <div class="barcode-field"></div>
  <div class="author-photo" role="img" aria-label="Freigestelltes Foto des Autors im braunen Sakko und hellblauen Hemd"></div>

  <svg class="typography" width="1200" height="927" viewBox="0 0 1200 927">
    <defs>
      <filter id="soft-shadow" x="-10%" y="-10%" width="120%" height="130%">
        <feDropShadow dx="2" dy="3" stdDeviation="2" flood-color="#000" flood-opacity="0.55"/>
      </filter>
    </defs>

    <!-- spine -->
    <g transform="translate(589,44) rotate(90)">
      <text class="author-line" x="0" y="0" font-size="24" textLength="236" lengthAdjust="spacingAndGlyphs">CORVIN HALLMARK</text>
    </g>
    <g transform="translate(589,434) rotate(90)">
      <text class="title-word" x="0" y="0" font-size="24" textLength="451" lengthAdjust="spacingAndGlyphs">BAUE KREDITE UND BLEIB FREI</text>
    </g>

    <!-- front cover -->
    <text class="author-line" x="650" y="60" font-size="21" textLength="507" lengthAdjust="spacingAndGlyphs">CORVIN HALLMARK - DER IMMOBILIENADVISOR</text>

    <g filter="url(#soft-shadow)">
      <text class="title-word" x="651" y="190" font-size="150" textLength="502" lengthAdjust="spacing">BAUE</text>
      <text class="title-word" x="651" y="280" font-size="93" textLength="506" lengthAdjust="spacingAndGlyphs">KREDITE</text>
      <text class="title-word" x="650" y="750" font-size="52">und</text>
      <text class="title-word" x="775" y="750" font-size="76" textLength="291" lengthAdjust="spacingAndGlyphs">BLEIB</text>
      <text class="title-word" x="651" y="885" font-size="172" textLength="502" lengthAdjust="spacing">FREI</text>
    </g>

    <g filter="url(#soft-shadow)">
      <text class="series-small" x="1156" y="379" font-size="19" text-anchor="end">GESPRÄCHE ÜBER</text>
      <text class="series-large" x="1156" y="423" font-size="28" text-anchor="end">IMMOBILIEN</text>
      <text class="subtitle" x="1024" y="545" font-size="18" text-anchor="middle">Lassen Sie uns freundschaftlich</text>
      <text class="subtitle" x="1024" y="568" font-size="18" text-anchor="middle">in entspannter Atmosphäre</text>
      <text class="subtitle" x="1024" y="591" font-size="18" text-anchor="middle">über Immobilien sprechen</text>
    </g>
  </svg>
</div>
</body>
</html>
```